Brightvale Solutions company needs a homepage design

We need a homepage designed for a new company based in Des Moines, IA called Go Brightvale Solutions. They sell Carewell Supplement plans to seniors. The design should communicate trust, security, be vibrant and easy to read with larger font and clear messages. The goal for visitors is to ultimately get a free quote and purchase a plan after a call from a licensed agent.

```html
<!DOCTYPE html>
<html lang="en">
<head>
<meta charset="utf-8">
<title>Brightvale Solutions — Carewell Supplement Plans</title>
<link href="https://fonts.googleapis.com/css2?family=Hind:wght@400;500;600&family=Lato:ital,wght@0,400;0,700;1,400&display=swap" rel="stylesheet">
<style>
:root{
  --blue:#1a5aab;
  --navy:#134b8f;
  --teal:#1f8b80;
  --teal-light:#2aa69b;
  --green:#3f9a6e;
  --ink:#222;
  --text:#444;
  --muted:#999;
  --grey-btn:#9a9a9a;
  --hero-a:#d9f1ec;
  --hero-b:#a9ddd2;
  --map-a:#e6e2d6;
  --map-b:#6aa6d8;
  --white:#fff;
}
*{box-sizing:border-box;margin:0;padding:0}
html,body{width:1200px;height:3125px;overflow:hidden}
body{position:relative;background:var(--white);font-family:"Lato",Arial,sans-serif;color:var(--text)}
.abs{position:absolute}
h1,h2,h3,.heading{font-family:"Hind",Arial,sans-serif}

/* header */
.brand{left:98px;top:12px;display:flex;align-items:center;gap:16px}
.brand-dot{width:64px;height:64px;border-radius:50%;background:var(--teal)}
.brand-name{font-family:"Hind",sans-serif;font-weight:500;font-size:30px;color:var(--blue);letter-spacing:.5px;white-space:nowrap}
.info{top:28px;display:flex;gap:12px;font-size:15px;line-height:20px;color:var(--ink);white-space:nowrap}
.info b{font-weight:700}
.info span{display:block;color:#555}
.nav{left:98px;top:96px;width:1002px;height:46px;background:var(--blue);display:flex;align-items:center;padding-left:30px;gap:36px}
.nav a{color:var(--white);text-decoration:none;font-size:14px;font-family:"Hind",sans-serif;font-weight:500;letter-spacing:.3px}

/* hero */
.hero{left:0;top:142px;width:1200px;height:525px;background:linear-gradient(90deg,var(--hero-a),var(--hero-b))}
.hero-photo{left:160px;top:142px;width:520px;height:525px;background:linear-gradient(180deg,#bfe3da,#7fc6cf)}
.hero-title{left:688px;top:298px;font-size:48px;font-weight:600;color:#223;white-space:nowrap}
.hero-text{left:692px;top:368px;width:380px;font-size:17px;line-height:25px;color:#667}
.btn{display:flex;align-items:center;justify-content:center;color:var(--white);font-weight:700;font-size:16px;font-family:"Hind",sans-serif;text-decoration:none}
.btn-quote{left:690px;top:458px;width:140px;height:42px;background:var(--teal)}
.btn-contact{left:840px;top:458px;width:156px;height:42px;background:var(--blue)}

/* services */
.section-title{width:1200px;left:0;text-align:center;font-size:46px;font-weight:500;color:var(--ink)}
.service{top:850px;width:240px;text-align:center}
.service .circle{width:146px;height:146px;margin:0 auto;border-radius:50%;background:var(--green);display:flex;align-items:center;justify-content:center}
.service h3{margin-top:26px;font-size:18px;line-height:22px;font-weight:500;color:var(--blue);text-transform:uppercase;height:44px;display:flex;align-items:center;justify-content:center}
.service p{margin-top:12px;font-size:12.5px;line-height:17px;color:#333}
.btn-more{left:490px;top:1192px;width:180px;height:41px;background:var(--grey-btn);font-size:13px;font-weight:500}

/* about */
.about{left:0;top:1327px;width:1200px;height:521px;background:var(--blue)}
.about-frame{left:100px;top:1475px;width:370px;height:292px;background:var(--teal)}
.about-photo{left:115px;top:1396px;width:511px;height:356px;background:linear-gradient(135deg,#f3e3d6,#c9d6d8)}
.about-kicker{left:664px;top:1380px;font-size:78px;font-weight:500;color:var(--teal-light);line-height:80px}
.about-title{left:665px;top:1458px;font-size:27px;font-weight:500;color:var(--white);letter-spacing:.5px;white-space:nowrap}
.about-text{left:665px;top:1506px;width:415px;font-size:14px;line-height:21px;color:var(--white)}
.about-text p+p{margin-top:21px}
.about-link{left:666px;top:1690px;font-size:14px;color:var(--white);text-decoration:underline}

/* testimonials */
.rule{left:583px;top:2052px;width:70px;height:4px;background:var(--teal-light)}
.quote{top:2115px;width:450px}
.quote .mark{position:absolute;left:0;top:0;font-family:Georgia,serif;font-size:52px;line-height:44px;color:var(--teal-light)}
.quote blockquote{margin-left:43px;font-style:italic;font-size:19.5px;line-height:28px;color:#777}
.author{display:flex;align-items:center;gap:18px;margin:12px 0 0 43px}
.avatar{width:50px;height:50px;border-radius:50%;background:#a98d76}
.author b{display:block;font-family:"Hind",sans-serif;font-weight:500;font-size:19px;color:var(--blue)}
.author span{font-size:12px;font-style:italic;color:#aaa}
.dots{left:603px;top:2376px;display:flex;gap:20px}
.dots i{width:10px;height:10px;border-radius:50%;background:#ccc;display:block}
.dots i.on{background:var(--blue)}

/* map + hours */
.map{left:0;top:2443px;width:1200px;height:374px;background:linear-gradient(120deg,var(--map-a) 0%,#d7e4d5 30%,var(--map-b) 60%,#dfe6d3 100%)}
.hours{left:100px;top:2443px;width:277px;height:374px;background:var(--navy);color:var(--white);padding:36px 34px}
.hours h3{font-size:19px;font-weight:600;letter-spacing:.3px;margin-bottom:14px;white-space:nowrap}
.hours table{width:100%;border-collapse:collapse;font-size:11.5px}
.hours td{padding:10px 0;border-bottom:1px solid rgba(255,255,255,.25)}
.hours td:first-child{font-weight:700;width:90px}
.hours tr:last-child td{border:none}
.hours .contact{margin-top:20px}
.hours .contact div{display:flex;align-items:center;gap:10px;font-size:11.5px;margin-top:12px}

/* footer */
.footer{left:0;top:2817px;width:1200px;height:308px;background:var(--teal)}
.foot-brand{left:52px;top:2852px;width:306px;text-align:center;color:var(--white)}
.foot-brand .dot{width:66px;height:66px;border-radius:50%;background:var(--white);margin:0 auto 14px;opacity:.9}
.foot-brand .name{font-family:"Hind",sans-serif;font-weight:500;font-size:24px;line-height:28px;white-space:nowrap}
.socials{left:100px;top:2988px;width:206px;display:flex;justify-content:center;gap:15px}
.socials i{width:34px;height:34px;border-radius:50%;border:2px solid rgba(255,255,255,.8);display:block}
.foot-col{top:2862px;color:var(--white)}
.foot-col h4{font-family:"Hind",sans-serif;font-size:15px;font-weight:600;letter-spacing:.5px;padding-bottom:9px;border-bottom:1px solid rgba(255,255,255,.35)}
.foot-col .row{display:flex;align-items:center;gap:10px;font-size:13px;margin-top:18px;white-space:nowrap}
.foot-col p{font-size:12.5px;line-height:19px;margin-top:24px}
.signup{display:flex;margin-top:14px}
.signup span{width:204px;height:32px;background:var(--white);color:#999;font-size:11px;display:flex;align-items:center;padding-left:12px}
.signup b{width:76px;height:32px;background:#3aa2c8;font-size:11px;display:flex;align-items:center;justify-content:center}
.copy{left:100px;top:3078px;font-size:12px;color:rgba(255,255,255,.8)}
</style>
</head>
<body>

<header>
  <div class="abs brand"><div class="brand-dot"></div><span class="brand-name">BRIGHTVALE SOLUTIONS</span></div>
  <div class="abs info" style="left:582px">
    <svg width="24" height="24" viewBox="0 0 24 24"><path d="M6 3l4 4-2 2a12 12 0 0 0 7 7l2-2 4 4-3 3C10 21 3 14 3 6z" fill="none" stroke="#3f9a6e" stroke-width="1.6"/></svg>
    <div><b>0800 4410 275</b><span>hello@brightvale.com</span></div>
  </div>
  <div class="abs info" style="left:768px">
    <svg width="24" height="28" viewBox="0 0 24 28"><path d="M12 26s-8-9-8-15a8 8 0 0 1 16 0c0 6-8 15-8 15z" fill="none" stroke="#3f9a6e" stroke-width="1.6"/><circle cx="12" cy="11" r="3" fill="none" stroke="#3f9a6e" stroke-width="1.6"/></svg>
    <div><b>88 Locust Street</b><span>Des Moines, IA 50309</span></div>
  </div>
  <div class="abs info" style="left:952px">
    <svg width="26" height="26" viewBox="0 0 26 26"><circle cx="13" cy="13" r="11" fill="none" stroke="#3f9a6e" stroke-width="1.6"/><path d="M13 7v6l4 3" fill="none" stroke="#3f9a6e" stroke-width="1.6"/></svg>
    <div><b>7:30 AM - 7:30 PM</b><span>Monday to Saturday</span></div>
  </div>
  <nav class="abs nav">
    <a href="#">HOME</a><a href="#">ABOUT US</a><a href="#">SERVICES</a><a href="#">GET A FREE QUOTE</a><a href="#">NEWS</a><a href="#">CONTACT US</a>
  </nav>
</header>

<section>
  <div class="abs hero"></div>
  <div class="abs hero-photo" role="img" aria-label="Cheerful nurse in blue scrubs with a stethoscope, flexing her arms in a bright clinic room"></div>
  <h1 class="abs hero-title">Carewell Solution</h1>
  <p class="abs hero-text">is a company passionate about creating healthy loving relationships, of all kinds.</p>
  <a class="abs btn btn-quote" href="#">Get A Quote</a>
  <a class="abs btn btn-contact" href="#">Contact Us</a>
</section>

<section>
  <h2 class="abs section-title" style="top:736px">Do you need help with:</h2>
  <div class="abs service" style="left:82px">
    <div class="circle"><svg width="60" height="50" viewBox="0 0 60 50"><rect x="6" y="8" width="16" height="34" rx="8" fill="none" stroke="#fff" stroke-width="3"/><line x1="6" y1="25" x2="22" y2="25" stroke="#fff" stroke-width="3"/><circle cx="38" cy="20" r="9" fill="#fff"/><circle cx="44" cy="36" r="8" fill="#fff"/></svg></div>
    <h3>Modern<br>Medicines</h3>
    <p>Lorem ipsum dolor sit amet, consectetur adipiscing elit. Aliquam quis ipsum dolor sit amet, consectetur adipiscing semper felis.</p>
  </div>
  <div class="abs service" style="left:326px">
    <div class="circle"><svg width="50" height="56" viewBox="0 0 50 56"><circle cx="25" cy="16" r="11" fill="none" stroke="#fff" stroke-width="3"/><path d="M5 54c0-14 8-22 20-22s20 8 20 22z" fill="none" stroke="#fff" stroke-width="3"/><path d="M20 40v6h10" fill="none" stroke="#fff" stroke-width="3"/></svg></div>
    <h3>Qualified Doctors<br>and Staff</h3>
    <p>Lorem ipsum dolor sit amet, consectetur adipiscing elit. Aliquam quis ipsum dolor sit amet, consectetur adipiscing semper felis.</p>
  </div>
  <div class="abs service" style="left:595px">
    <div class="circle"><svg width="64" height="60" viewBox="0 0 64 60"><path d="M20 38L46 12l6 6-26 26z" fill="#fff"/><line x1="49" y1="15" x2="58" y2="6" stroke="#fff" stroke-width="4"/><line x1="20" y1="38" x2="14" y2="44" stroke="#fff" stroke-width="3"/><path d="M10 46c-3 5-4 7-4 9a4 4 0 0 0 8 0c0-2-1-4-4-9z" fill="#fff"/></svg></div>
    <h3>Ambulance<br>Services</h3>
    <p>Lorem ipsum dolor sit amet, consectetur adipiscing elit. Aliquam quis ipsum dolor sit amet, consectetur adipiscing semper felis.</p>
  </div>
  <div class="abs service" style="left:849px">
    <div class="circle"><svg width="64" height="44" viewBox="0 0 64 44"><path d="M4 6h36v30H4zM40 14h12l8 10v12H40z" fill="#fff"/><rect x="17" y="12" width="6" height="18" fill="#3f9a6e"/><rect x="11" y="18" width="18" height="6" fill="#3f9a6e"/><circle cx="14" cy="38" r="5" fill="#3f9a6e" stroke="#fff" stroke-width="2"/><circle cx="48" cy="38" r="5" fill="#3f9a6e" stroke="#fff" stroke-width="2"/></svg></div>
    <h3>Ambulance<br>Services</h3>
    <p>Lorem ipsum dolor sit amet, consectetur adipiscing elit. Aliquam quis ipsum dolor sit amet, consectetur adipiscing semper felis.</p>
  </div>
  <a class="abs btn btn-more" href="#">READ MORE</a>
</section>

<section>
  <div class="abs about"></div>
  <div class="abs about-frame"></div>
  <div class="abs about-photo" role="img" aria-label="Smiling senior couple embracing"></div>
  <h2 class="abs about-kicker">ABOUT</h2>
  <h3 class="abs about-title">BRIGHTVALE SOLUTIONS</h3>
  <div class="abs about-text">
    <p>Lorem ipsum dolor sit amet, consectetur adipiscing. Nunc pharetra interdum iaculis. Vestibulum semper mauris felis, euismod velit consequat sed. Proin porttitor purus in odio egestas, sed efficitur nibh ultrices.</p>
    <p>Morbi mattis sollicitudin libero ut finibus. Morbi imperdiet tortor ex, ut convallis nisi vestibulum eget. Phasellus hendrerit ut erat eget pharetra.</p>
  </div>
  <a class="abs about-link" href="#">Read More</a>
</section>

<section>
  <h2 class="abs section-title" style="top:1952px">Client Testimonials</h2>
  <div class="abs rule"></div>
  <div class="abs quote" style="left:115px">
    <span class="mark">&ldquo;</span>
    <blockquote>The costs of treatments are very reasonable at Brightvale and I have always been impressed with the results. The fully medically qualified team at the clinic are professional, friendly and trustworthy.</blockquote>
    <div class="author"><div class="avatar" role="img" aria-label="Portrait of the patient"></div><div><b>Nora Pell</b><span>Patient</span></div></div>
  </div>
  <div class="abs quote" style="left:615px">
    <span class="mark">&ldquo;</span>
    <blockquote>Dr. Halvorsen is a wonderful Doctor, who makes you feel important and who takes time to listen, which most doctors don't do. Loved him from the first visit! Very professional assistance.</blockquote>
    <div class="author"><div class="avatar" role="img" aria-label="Portrait of the patient"></div><div><b>Owen Marsh</b><span>Patient</span></div></div>
  </div>
  <div class="abs dots"><i class="on"></i><i></i></div>
</section>

<section>
  <div class="abs map" role="img" aria-label="City street map with a location pin marking the office"></div>
  <div class="abs hours">
    <h3>WORKING HOURS</h3>
    <table>
      <tr><td>MON – WED</td><td>8:00 AM – 7:00 PM</td></tr>
      <tr><td>THU</td><td>8:00 AM – 5:00 PM</td></tr>
      <tr><td>FRI</td><td>8:00 AM – 5:00 PM</td></tr>
      <tr><td>SAT – SUN</td><td>Closed</td></tr>
    </table>
    <div class="contact">
      <h3>CONTACT DETAILS</h3>
      <div><svg width="12" height="14" viewBox="0 0 12 14"><path d="M6 13S1 8 1 5a5 5 0 0 1 10 0c0 3-5 8-5 8z" fill="none" stroke="#fff"/></svg>Grand Avenue 12, IA, US</div>
      <div><svg width="12" height="12" viewBox="0 0 24 24"><path d="M6 3l4 4-2 2a12 12 0 0 0 7 7l2-2 4 4-3 3C10 21 3 14 3 6z" fill="#fff"/></svg>+0800 5512 9034</div>
    </div>
  </div>
</section>

<footer>
  <div class="abs footer"></div>
  <div class="abs foot-brand"><div class="dot"></div><div class="name">BRIGHTVALE SOLUTIONS</div></div>
  <div class="abs socials"><i></i><i></i><i></i><i></i></div>
  <div class="abs foot-col" style="left:443px;width:300px">
    <h4>CONTACT US</h4>
    <div class="row"><svg width="16" height="16" viewBox="0 0 24 24"><path d="M6 3l4 4-2 2a12 12 0 0 0 7 7l2-2 4 4-3 3C10 21 3 14 3 6z" fill="#7fe08a"/></svg>1-800-5550-142, 1-800-5550-187</div>
    <div class="row"><svg width="14" height="16" viewBox="0 0 12 14"><path d="M6 13S1 8 1 5a5 5 0 0 1 10 0c0 3-5 8-5 8z" fill="#7fe08a"/></svg>410 Keo Way Des Moines, IA 50309-2211 USA</div>
    <div class="row" style="color:#7fe08a"><svg width="16" height="12" viewBox="0 0 16 12"><rect x="1" y="1" width="14" height="10" fill="none" stroke="#7fe08a"/><path d="M1 1l7 6 7-6" fill="none" stroke="#7fe08a"/></svg>care@brightvale.org</div>
  </div>
  <div class="abs foot-col" style="left:815px;width:285px">
    <h4>NEWSLETTER</h4>
    <p>Enter your email address to receive up-to-date news, new patient information and other useful stuff, delivered right to your inbox.</p>
    <div class="signup"><span>Your e-mail...</span><b>SUBSCRIBE</b></div>
  </div>
  <div class="abs copy">© 2017 All Rights Reserved. Privacy Policy</div>
</footer>

</body>
</html>
```